Vantor Roving Car Wash and Detail Services, 'needs a logo and card design'

I need a logo and Card design for a new company based in Perth Western Australia called, 'Vantor Roving Car Wash and Detail Services'. I want to offer a mobile car wash and detail service across all the Perth metropolitan areas at lower prices, and offer more reliability. I would like to see designs with colours such as red, white, and black. The final design should communicate trust reliability and confidence in the services I can provide. The card must include my first name 'Oswin' and my mobile number '0471208356' for an obligation free quote.
Updates

Target Market(s)

Aimed at anyone who owns and drives a motor vehicle.

Industry/Entity Type

It Company

Contact Information for Business Card

Business Name'Vantor Roving Car Wash and Detail Services', My first name 'Oswin', and my mobile phone '0471208356' for an obligation free quote.

Font styles to use
Serif
Decorative
Script

Colors
ffffff
000000
d3d3d3
ec1f27
7f7f7f

Requirements
Must have
• Business Name'Vantor Roving Car Wash and Detail Services', My first name 'Oswin', and my mobile phone '0471208356' for an obligation free quote.
• Logo design
Nice to have
• A slogan, such as 'I come to you, and wash your car wherever you are' to let customers know I am at their service.
• Car design 'shine and clean feeling'

```html
<!DOCTYPE html>
<html lang="en">
<head>
<meta charset="utf-8">
<title>Vantor Roving Car Wash and Detail Services – Business Card</title>
<link href="https://fonts.googleapis.com/css2?family=Montserrat:wght@700&family=Oswald:wght@400;500&display=swap" rel="stylesheet">
<style>
  :root {
    --backdrop: #e6e6e6;
    --card-white: #ffffff;
    --brand-red: #ec1f27;
    --red-deep: #c2151c;
    --red-dark: #a80f15;
    --red-light: #f4474d;
    --ink: #1f1f1f;
    --band-dark: #262626;
    --band-mid: #3a3a3a;
    --text-light: #ffffff;
  }
  html, body {
    margin: 0;
    padding: 0;
    width: 1200px;
    height: 826px;
    overflow: hidden;
    background: var(--backdrop);
  }
  .canvas {
    position: relative;
    width: 1200px;
    height: 826px;
  }
  .business-card {
    position: absolute;
    left: 50px;
    top: 76px;
    width: 1100px;
    height: 674px;
    background: var(--card-white);
    overflow: hidden;
  }
  .card-graphics {
    position: absolute;
    inset: 0;
  }
  .contact-block {
    position: absolute;
    left: 62px;
    top: 62px;
    color: var(--ink);
  }
  .contact-name {
    margin: 0;
    font-family: "Montserrat", sans-serif;
    font-weight: 700;
    font-size: 38px;
    line-height: 1;
  }
  .contact-phone {
    display: flex;
    align-items: center;
    gap: 16px;
    margin-top: 40px;
    font-family: "Oswald", sans-serif;
    font-weight: 400;
    font-size: 60px;
    line-height: 1;
  }
  .phone-icon {
    width: 30px;
    height: 44px;
  }
  .quote-note {
    margin: 28px 0 0;
    font-family: "Oswald", sans-serif;
    font-weight: 400;
    font-size: 31px;
    line-height: 1.3;
  }
  .brand-seal {
    position: absolute;
    left: 563px;
    top: 70px;
    width: 476px;
    height: 476px;
    border-radius: 50%;
    background: var(--card-white);
    display: flex;
    align-items: center;
    justify-content: center;
    text-align: center;
  }
  .brand-name {
    margin: 0;
    width: 330px;
    font-family: "Oswald", sans-serif;
    font-weight: 500;
    font-size: 40px;
    line-height: 1.2;
    text-transform: uppercase;
    color: var(--brand-red);
  }
  .slogan-band {
    position: absolute;
    left: 0;
    bottom: 0;
    width: 100%;
    height: 75px;
    background: linear-gradient(90deg, var(--band-dark), var(--band-mid));
    display: flex;
    align-items: center;
    justify-content: center;
  }
  .slogan {
    margin: 0;
    font-family: "Oswald", sans-serif;
    font-weight: 400;
    font-size: 32px;
    color: var(--text-light);
  }
</style>
</head>
<body>
<main class="canvas">
  <section class="business-card">
    <svg class="card-graphics" width="1100" height="674" viewBox="0 0 1100 674" aria-hidden="true">
      <polygon points="513,0 1100,0 1100,599 270,599 640,430 660,140" fill="var(--brand-red)"/>
      <polygon points="660,0 1100,0 1100,150 900,260" fill="var(--red-deep)"/>
      <polygon points="760,0 960,0 860,120" fill="var(--red-light)"/>
      <polygon points="1100,360 1100,599 820,599 960,470" fill="var(--red-dark)"/>
      <polygon points="270,599 640,430 700,599" fill="var(--red-deep)"/>
    </svg>

    <div class="contact-block">
      <h1 class="contact-name">Oswin</h1>
      <div class="contact-phone">
        <svg class="phone-icon" viewBox="0 0 30 44" aria-hidden="true">
          <rect x="8" y="0" width="4" height="8" rx="1.5" fill="var(--brand-red)"/>
          <rect x="2" y="7" width="26" height="36" rx="6" fill="var(--brand-red)"/>
          <rect x="7" y="13" width="16" height="10" rx="2" fill="var(--card-white)"/>
          <circle cx="10" cy="30" r="2" fill="var(--card-white)"/>
          <circle cx="15" cy="30" r="2" fill="var(--card-white)"/>
          <circle cx="20" cy="30" r="2" fill="var(--card-white)"/>
          <circle cx="10" cy="36" r="2" fill="var(--card-white)"/>
          <circle cx="15" cy="36" r="2" fill="var(--card-white)"/>
          <circle cx="20" cy="36" r="2" fill="var(--card-white)"/>
        </svg>
        <span>0471208356</span>
      </div>
      <p class="quote-note">call for an<br>obligation free quote</p>
    </div>

    <div class="brand-seal">
      <p class="brand-name">Vantor Roving Car Wash and Detail Services</p>
    </div>

    <footer class="slogan-band">
      <p class="slogan">I come to you, and wash your car wherever you are</p>
    </footer>
  </section>
</main>
</body>
</html>
```